Mechanical Engineer Business Card Design (Unemployed)

I am unemployed and actively looking for a job in Canada. I will be using this business card when I meet potential employers or in networking events.I would love to have the engraved writing style (as if it is engraved on the card). Some examples attached.I would love to have a personalized logo that represents my 2 majors. The final design should have a professional look that can stand out if attached to a resume. Jobs I am applying for are in construction, mining, oil and gas, Aerospace, manufacturing and whatever field I can be integrated in.A metallic look on the back is ok. but the front have to be sort of can be written on. you can also try to add my profilelink profile https://ca.profilelink.example/in/tomasvelder
On the front or back, I would love to have the symbol of mail and phone rather than the words. that saves spaceAmaze me guys.

Target Market(s)

Engineering

Industry/Entity Type

Engineering

Contact Information for Business Card

Tomas Velder
Mechanical Engineer

Phone number: +1 (555) 014 - 2738
email: veldertomas@mailbox.example

Requirements
Must have
• PERSONALIZED and brand new Simple Logo
• Professional look
• Engraved writing for the name
• Help stand out when attached on CV
Nice to have
• Metallic back look

```html
<!DOCTYPE html>
<html lang="en">
<head>
<meta charset="utf-8">
<title>Tomas Velder – Business Card</title>
<link href="https://fonts.googleapis.com/css2?family=Michroma&display=swap" rel="stylesheet">
<style>
  :root {
    --backdrop: #67abbf;
    --card: #f3f3f3;
    --accent-red: #a3161d;
    --ink: #2b2b2b;
    --rule: #6a6a6a;
    --shadow: rgba(20, 60, 75, 0.35);
  }
  * { margin: 0; padding: 0; box-sizing: border-box; }
  html, body {
    width: 1200px; height: 814px; overflow: hidden;
    background: var(--backdrop);
    font-family: "Michroma", sans-serif;
  }
  .canvas {
    width: 1200px; height: 814px;
    display: flex; align-items: center; justify-content: center; gap: 60px;
  }
  .card {
    width: 520px; height: 297px;
    background: var(--card);
    box-shadow: 0 10px 30px var(--shadow);
    position: relative;
  }
  .engraved { text-shadow: 0 1px 0 rgba(255,255,255,0.9), 0 -1px 0 rgba(0,0,0,0.18); }

  /* Front card */
  .card--front {
    display: flex; flex-direction: column; align-items: center; justify-content: center;
  }
  .brand-mark {
    display: flex; align-items: center; gap: 10px;
    margin-bottom: 16px;
  }
  .brand-mark__dot {
    width: 18px; height: 18px; border-radius: 50%;
    background: var(--ink);
  }
  .brand-mark__name {
    font-size: 15px; color: var(--accent-red); letter-spacing: 2px;
  }
  .front-name {
    font-size: 22px; color: var(--accent-red); letter-spacing: 3px;
    font-variant: small-caps;
  }
  .front-title {
    margin-top: 6px;
    display: flex; align-items: center; gap: 10px;
    font-size: 10px; color: var(--ink); letter-spacing: 2px; font-variant: small-caps;
  }
  .front-title::before, .front-title::after {
    content: ""; width: 50px; height: 1px; background: var(--rule);
  }

  /* Back card */
  .card--back {
    display: flex; align-items: center; padding: 0 32px;
  }
  .back-mark {
    width: 170px; display: flex; align-items: center; justify-content: center; gap: 10px;
  }
  .back-mark .brand-mark__dot { width: 22px; height: 22px; }
  .back-mark .brand-mark__name { font-size: 17px; }
  .divider {
    width: 1px; height: 150px; background: var(--rule); margin: 0 24px;
  }
  .contact { display: flex; flex-direction: column; }
  .contact__name {
    font-size: 15px; color: var(--accent-red); letter-spacing: 2px; font-variant: small-caps;
  }
  .contact__title {
    font-size: 8px; color: var(--ink); letter-spacing: 2px; font-variant: small-caps;
    margin-top: 3px; margin-bottom: 20px;
  }
  .contact__line {
    display: flex; align-items: center; gap: 8px;
    font-size: 9px; color: var(--ink); letter-spacing: 1.5px;
    margin-bottom: 10px;
  }
  .contact__line--email { font-size: 7.5px; font-variant: small-caps; letter-spacing: 1px; }
  .contact__icon { width: 14px; height: 14px; flex: none; }
</style>
</head>
<body>
<main class="canvas">
  <section class="card card--front" aria-label="Card front">
    <div class="brand-mark">
      <span class="brand-mark__dot"></span>
      <span class="brand-mark__name engraved">Velder</span>
    </div>
    <h1 class="front-name engraved">Tomas Velder</h1>
    <p class="front-title engraved">Mechanical Engineer</p>
  </section>

  <section class="card card--back" aria-label="Card back">
    <div class="back-mark">
      <span class="brand-mark__dot"></span>
      <span class="brand-mark__name engraved">Velder</span>
    </div>
    <div class="divider"></div>
    <div class="contact">
      <h2 class="contact__name engraved">Tomas Velder</h2>
      <p class="contact__title engraved">Mechanical Engineer</p>
      <p class="contact__line engraved">
        <svg class="contact__icon" viewBox="0 0 14 14" aria-hidden="true">
          <circle cx="7" cy="7" r="7" fill="#a3161d"/>
          <rect x="4.6" y="3" width="4.8" height="8" rx="0.8" fill="none" stroke="#fff" stroke-width="1"/>
          <line x1="6.2" y1="9.6" x2="7.8" y2="9.6" stroke="#fff" stroke-width="0.8"/>
        </svg>
        +1 (555) 014 - 2738
      </p>
      <p class="contact__line contact__line--email engraved">
        <svg class="contact__icon" viewBox="0 0 14 14" aria-hidden="true">
          <circle cx="7" cy="7" r="7" fill="#a3161d"/>
          <rect x="3.5" y="4.5" width="7" height="5" fill="none" stroke="#fff" stroke-width="0.9"/>
          <polyline points="3.5,4.5 7,7.3 10.5,4.5" fill="none" stroke="#fff" stroke-width="0.9"/>
        </svg>
        veldertomas@mailbox.example
      </p>
    </div>
  </section>
</main>
</body>
</html>
```